The Harbourlight CV consultant

The service is premium. It is aimed at people 18-30, so students and those looking to change their first job, principally in the UK but also global. It is offering a very personalised CV writing service and is much more expensive than others on offer. I am very keen that it should look simple and premium. It needs to look very professional, reflecting the aspirational jobs that the clients will be applying for.
If there were three words that summed it up: modern, clean, premium.
I am waiting for all the testimonials to come in but they need to form a major part of the website.
I am also waiting for the full logo design files so that I can upload them. In the meantime there is a copy of the logo.
Thoughts to help those yet to send a design...
This is a premium service and some of the designs have looked very generic. The focus needs to be on quality and the process mentioned in the brief. The partnership and the advantages it brings are crucial but few have mentioned that.

```html
<!DOCTYPE html>
<html lang="en">
<head>
<meta charset="utf-8">
<title>The Harbourlight CV Consultant</title>
<link href="https://fonts.googleapis.com/css2?family=Roboto:wght@400;500;700&family=Roboto+Slab:wght@400;600;700&display=swap" rel="stylesheet">
<style>
:root{
  --blue:#0b65bf;
  --blue-dark:#0a4f9a;
  --ink:#1b1b1b;
  --grey:#8a8a8a;
  --text:#3a3a3a;
  --soft:#f1f3fa;
  --footer:#1c1c1e;
  --white:#ffffff;
}
*{margin:0;padding:0;box-sizing:border-box}
html,body{width:1200px;height:4082px;overflow:hidden;background:var(--white)}
body{font-family:"Roboto",Arial,sans-serif;color:var(--text)}
.page{position:relative;width:1200px;height:4082px;overflow:hidden}
.abs{position:absolute}
.serif{font-family:"Roboto Slab",Georgia,serif}
svg{display:block}

/* top bar */
.topbar{left:0;top:0;width:1200px;height:35px}
.topbar-info{top:0;left:680px;height:35px;display:flex;align-items:center;gap:16px;color:#fff;font-size:12.5px}
.topbar-info span{display:flex;align-items:center;gap:8px}

/* header */
.logo{left:111px;top:48px;display:flex;align-items:center;gap:12px;font-family:"Roboto Slab",Georgia,serif;font-weight:600;color:var(--blue);font-size:21px;line-height:1.1;width:280px}
.logo-mark{width:16px;height:16px;background:var(--blue);flex:none}
.nav{left:442px;top:80px;display:flex;gap:29px;font-size:13.5px;font-weight:700;color:var(--ink);letter-spacing:.2px}
.nav .active{color:var(--blue)}
.social{display:flex;gap:9px}
.social i{display:block;width:36px;height:36px;border-radius:50%;background:#fff;box-shadow:0 2px 8px rgba(0,0,0,.15)}
.social i.on{background:var(--blue)}
.header-social{left:966px;top:71px}

/* hero */
.hero-photo{left:0;top:138px;width:1200px;height:773px;background:linear-gradient(100deg,#e9eef6 0%,#f6f8fb 35%,#dfe8f3 60%,#b9cde3 100%)}
.hero-fade{left:0;top:138px;width:760px;height:773px;background:linear-gradient(90deg,rgba(255,255,255,.9),rgba(255,255,255,0))}
.hero-title{left:111px;top:298px;font-size:47px;line-height:57px;font-weight:700;color:var(--ink);letter-spacing:.5px}
.hero-title .light{font-weight:400;color:#555}
.checks{left:111px;top:434px;list-style:none;font-size:19.5px;color:var(--ink)}
.checks li{display:flex;align-items:center;gap:28px;height:43px}
.btn{display:inline-flex;align-items:center;gap:8px;font-weight:700;font-size:14px;text-transform:uppercase;border-radius:2px}
.btn-blue{background:var(--blue);color:#fff;box-shadow:0 4px 10px rgba(11,101,191,.3)}
.btn-white{background:#fff;color:var(--ink)}
.hero-btn{left:111px;top:626px;height:48px;padding:0 20px}

/* intro */
.tile{background:linear-gradient(135deg,#b8c7d8,#e7ebf0)}
.intro-heading{left:644px;top:994px;width:440px;font-size:27px;line-height:38px;font-weight:600;color:var(--ink)}
.intro-heading .light{font-weight:400;color:#777}
.rule{height:3px;background:var(--blue)}
.intro-copy{left:644px;top:1180px;width:444px;font-size:14.5px;line-height:26px;color:#444;text-align:justify}
.intro-btn{left:644px;top:1343px;height:46px;padding:0 21px}

/* approach */
.approach{left:0;top:1525px;width:1200px;height:818px;background:var(--soft)}
.approach-title{left:0;top:1594px;width:1200px;text-align:center;font-size:34px;line-height:45px;font-weight:600;color:var(--ink)}
.approach-title .light{font-weight:400;color:#888}
.center-copy{left:140px;width:920px;text-align:center;font-size:18px;line-height:28px;color:#333}
.card{top:1899px;width:304px;height:239px;background:#fff;border-radius:10px;box-shadow:0 6px 18px rgba(30,50,100,.12);text-align:center}
.card .badge{width:88px;height:88px;border-radius:50%;background:var(--blue);margin:38px auto 0;display:flex;align-items:center;justify-content:center}
.card h3{margin-top:24px;font-size:20px;line-height:30px;font-weight:700;color:#4a4a4a;text-transform:uppercase}

/* partnership */
.partner{left:0;top:2343px;width:1200px;height:729px;background:radial-gradient(circle at 20% 30%,#1d7bd6 0%,#0b65bf 45%,#0a56a8 100%)}
.partner-title{left:0;top:2415px;width:1200px;text-align:center;color:#fff;font-size:40px;font-weight:600}
.partner-title .light{font-weight:400}
.partner-lead{left:140px;top:2500px;width:920px;text-align:center;color:#fff;font-size:17px;line-height:28px;font-weight:500}
.partner-copy{left:111px;top:2673px;width:450px;color:#fff;font-size:17px;line-height:28px;font-weight:500}
.partner-copy p+p{margin-top:16px}
.partner-btn{left:111px;top:2885px;height:46px;padding:0 26px}
.partner-photo{left:599px;top:2628px;width:490px;height:360px;background:linear-gradient(135deg,#c9d5e0 0%,#8e9fb0 45%,#4a5665 100%)}

/* testimonials */
.test-title{left:0;top:3175px;width:1200px;text-align:center;font-size:40px;font-weight:600;color:var(--ink)}
.tcard{top:3273px;width:305px;height:258px;background:#fff;box-shadow:0 5px 16px rgba(0,0,0,.1);padding:26px 24px}
.stars{color:#f2a900;font-size:15px;letter-spacing:2px}
.tcard p{margin-top:8px;font-size:14px;line-height:23px;color:#444;text-align:justify}
.tcard hr{border:0;border-top:1px solid #ddd;margin:16px 0 14px}
.person{display:flex;align-items:center;gap:20px}
.avatar{width:56px;height:56px;border-radius:50%;background:linear-gradient(135deg,#d9c6b5,#a88f7a)}
.person b{display:block;color:var(--blue);font-size:16px}
.person small{font-size:13px;color:#444}
.dots{left:560px;top:3571px;display:flex;gap:11px}
.dots i{width:11px;height:11px;border-radius:50%;background:#cfd3db}
.dots i.on{background:var(--blue)}

/* footer */
.fcol{top:3794px;color:#fff}
.fcol h4{font-size:17px;font-weight:700;margin-bottom:17px;text-transform:uppercase}
.fcol ul{list-style:none;font-size:14px}
.fcol li{display:flex;align-items:center;gap:18px;height:38.5px}
.contact-item{display:flex;gap:18px;margin-bottom:16px;font-size:12.5px;line-height:20px}
.contact-item b{font-size:14px;display:block}
.news{left:805px;top:3839px;width:282px;height:46px;background:#fff;display:flex;border:2px solid var(--blue)}
.news span{flex:1;padding-left:16px;line-height:42px;font-size:14px;color:#666}
.news b{width:106px;background:var(--blue);color:#fff;font-size:14px;line-height:42px;text-align:center}
.footer-social{left:805px;top:3905px}
.footer-social i{background:#fff;box-shadow:none}
.footer-social i.on{background:var(--blue)}
.copy{left:0;top:4040px;width:1200px;text-align:center;color:#fff;font-size:12px}
.copyline{left:0;top:4022px;width:1200px;height:1px;background:#333}
</style>
</head>
<body>
<div class="page">

  <!-- top bar -->
  <svg class="abs topbar" width="1200" height="35"><rect width="1200" height="6" fill="#1c1c1e"/><polygon points="638,0 1200,0 1200,35 672,35" fill="#1c1c1e"/></svg>
  <div class="abs topbar-info">
    <span><svg width="12" height="12" viewBox="0 0 24 24"><path fill="#2c8be6" d="M6.6 10.8a15 15 0 006.6 6.6l2.2-2.2c.3-.3.7-.4 1-.2 1.1.4 2.3.6 3.6.6.6 0 1 .4 1 1V20c0 .6-.4 1-1 1A17 17 0 013 4c0-.6.4-1 1-1h3.5c.6 0 1 .4 1 1 0 1.3.2 2.5.6 3.6.1.3 0 .7-.2 1z"/></svg>+1 (888) 888 8888</span>
    <span>|</span>
    <span><svg width="13" height="11" viewBox="0 0 24 18"><path fill="#2c8be6" d="M0 0h24v18H0zM2 2l10 7 10-7z"/></svg>info@harbourlightcv.co.uk</span>
  </div>

  <!-- header -->
  <div class="abs logo"><span class="logo-mark"></span><span>The Harbourlight CV Consultant</span></div>
  <nav class="abs nav"><span class="active">HOME</span><span>ABOUT US</span><span>SERVICES</span><span>TESTIMONIALS</span><span>CONTACT US</span></nav>
  <div class="abs social header-social" aria-label="Social links"><i class="on"></i><i></i><i></i></div>

  <!-- hero -->
  <div class="abs hero-photo" role="img" aria-label="Photo of a consultant's hands reviewing CV documents on a desk"></div>
  <div class="abs hero-fade"></div>
  <svg class="abs" style="left:0;top:138px" width="1200" height="775">
    <line x1="0" y1="120" x2="190" y2="120" stroke="#0b65bf" stroke-width="2"/>
    <circle cx="198" cy="122" r="13" fill="#0b65bf"/>
    <polygon points="869,683 1200,639 1200,770" fill="#0b65bf"/>
    <polygon points="0,775 240,765 1200,770 1200,775" fill="#fff"/>
    <polygon points="240,742 869,683 1200,770 240,765" fill="#fff" opacity=".55"/>
  </svg>
  <h1 class="abs hero-title serif">THE HARBOURLIGHT<br><span class="light">CV CONSULTANT</span></h1>
  <ul class="abs checks">
    <li><svg width="19" height="17" viewBox="0 0 24 22"><rect x="1" y="4" width="17" height="17" rx="2" fill="none" stroke="#0b65bf" stroke-width="2.5"/><path d="M6 11l5 5L23 3" fill="none" stroke="#0b65bf" stroke-width="3"/></svg>Is your current CV not getting you results?</li>
    <li><svg width="19" height="17" viewBox="0 0 24 22"><rect x="1" y="4" width="17" height="17" rx="2" fill="none" stroke="#0b65bf" stroke-width="2.5"/><path d="M6 11l5 5L23 3" fill="none" stroke="#0b65bf" stroke-width="3"/></svg>Do you want to create a CV that stands out from the crowd?</li>
    <li><svg width="19" height="17" viewBox="0 0 24 22"><rect x="1" y="4" width="17" height="17" rx="2" fill="none" stroke="#0b65bf" stroke-width="2.5"/><path d="M6 11l5 5L23 3" fill="none" stroke="#0b65bf" stroke-width="3"/></svg>Do you want to get a job more quickly?</li>
    <li><svg width="19" height="17" viewBox="0 0 24 22"><rect x="1" y="4" width="17" height="17" rx="2" fill="none" stroke="#0b65bf" stroke-width="2.5"/><path d="M6 11l5 5L23 3" fill="none" stroke="#0b65bf" stroke-width="3"/></svg>Do you want to earn more for the job your searching for?</li>
  </ul>
  <div class="abs btn btn-blue hero-btn">Get Started <svg width="14" height="14" viewBox="0 0 16 16"><circle cx="8" cy="8" r="7" fill="#fff"/><path d="M6 4.5L9.5 8 6 11.5" stroke="#0b65bf" stroke-width="2" fill="none"/></svg></div>

  <!-- intro -->
  <svg class="abs" style="left:230px;top:1050px" width="280" height="315">
    <polygon points="204,3 274,3 274,73 254,73 254,23 204,23" fill="#0b65bf" transform="translate(-10,0)"/>
    <polygon points="204,3 244,3 204,43" fill="#0b65bf" transform="translate(-10,20)"/>
    <polygon points="3,310 3,240 23,240 23,290 73,290" fill="#5a5a5a"/>
    <polygon points="23,270 63,270 23,310" fill="#5a5a5a" opacity=".8"/>
  </svg>
  <div class="abs tile" style="left:111px;top:997px;width:216px;height:211px" role="img" aria-label="Photo of a smiling young professional at a laptop"></div>
  <div class="abs tile" style="left:334px;top:1087px;width:134px;height:121px" role="img" aria-label="Photo of hands writing on a document"></div>
  <div class="abs tile" style="left:260px;top:1217px;width:133px;height:116px" role="img" aria-label="Photo of a businesswoman holding papers in an office"></div>
  <div class="abs tile" style="left:401px;top:1217px;width:179px;height:178px" role="img" aria-label="Photo of a meeting over documents"></div>

  <h2 class="abs intro-heading serif">IF SO THEN INVEST IN A CV WRITING PARTNERSHIP WITH OLIVER, <span class="light">THE HARBOURLIGHT CV CONSULTANT.</span></h2>
  <div class="abs rule" style="left:644px;top:1147px;width:75px"></div>
  <p class="abs intro-copy">But first read the testimonials. These are real results from real people. They invested in the partnership approach, and they're delighted because it works. The blurb that follows is not as important as what they say – I'd love it if you were the next person to appear in these testimonials. .</p>
  <div class="abs btn btn-blue intro-btn">Learn More <svg width="14" height="14" viewBox="0 0 16 16"><circle cx="8" cy="8" r="7" fill="#fff"/><path d="M6 4.5L9.5 8 6 11.5" stroke="#0b65bf" stroke-width="2" fill="none"/></svg></div>

  <!-- approach -->
  <div class="abs approach"></div>
  <h2 class="abs approach-title serif">PEOPLE I WORK WITH GET A JOB<br>SOONER AND <span class="light">GET A HIGHER PAID JOB.</span></h2>
  <p class="abs center-copy" style="top:1726px">Working with me is personalised, it's a partnership. Together we will build a great CV that will present you in the best way possible, it will increase the chances of you securing the job you want.</p>
  <p class="abs center-copy" style="top:1799px">And you'll also get this. As a result of my approach everyone I've worked with is better prepared for interview. Our partnership will</p>

  <div class="abs card" style="left:111px">
    <div class="badge"><svg width="48" height="48" viewBox="0 0 48 48" fill="none" stroke="#fff" stroke-width="2"><circle cx="24" cy="14" r="5"/><circle cx="14" cy="18" r="3.5"/><circle cx="34" cy="18" r="3.5"/><path d="M17 28c0-5 3-7 7-7s7 2 7 7"/><path d="M4 24l8 14h10M44 24l-8 14H26"/></svg></div>
    <h3>Increase Self<br>Awareness</h3>
  </div>
  <div class="abs card" style="left:448px">
    <div class="badge"><svg width="48" height="48" viewBox="0 0 48 48" fill="none" stroke="#fff" stroke-width="2"><rect x="6" y="6" width="24" height="16"/><path d="M10 18l5-5 4 3 6-6"/><circle cx="37" cy="14" r="4"/><path d="M31 30c0-4 3-6 6-6s6 2 6 6"/><circle cx="12" cy="32" r="3"/><circle cx="24" cy="32" r="3"/><path d="M6 44c0-4 3-6 6-6s6 2 6 6M18 44c0-4 3-6 6-6s6 2 6 6"/></svg></div>
    <h3>Improve<br>Presentation Skills</h3>
  </div>
  <div class="abs card" style="left:785px">
    <div class="badge"><svg width="48" height="48" viewBox="0 0 48 48" fill="none" stroke="#fff" stroke-width="2"><path d="M14 42V24h6l6-12c3 0 4 2 3 6l-1 4h10c2 0 4 2 3 4l-3 12c-1 3-3 4-5 4H14zM6 24h8v18H6z"/><path d="M30 6l2 3 3-1-1 3 3 2-3 1v3l-3-2M38 4v3"/></svg></div>
    <h3>Build the Right Sort<br>of Confidence</h3>
  </div>

  <p class="abs center-copy" style="top:2183px">And as a result you'll impress at interview. You'll develop a language and way of expressing yourself that shows the very best of you. And as that language sinks in and becomes part of you, you project a genuine confidence, quietly powerful, that recruiters will want in their teams.</p>

  <!-- partnership -->
  <div class="abs partner"></div>
  <h2 class="abs partner-title serif">THE <span class="light">PARTNERSHIP</span></h2>
  <div class="abs" style="left:563px;top:2468px;width:74px;height:3px;background:#fff"></div>
  <p class="abs partner-lead">The key to all this success is the partnership. Over four sessions we will, together, build a CV. You will get me, no one else, working with you for four sessions. There is a formula for success but it's not formulaic. Your CV will be personal, you will shine through. Your CV will be elevated above the crowd.</p>
  <div class="abs partner-copy">
    <p>I offer a premium service, very different to other offerings - so if like those in the testimonials, you get that job sooner, get a higher paid job, the investment is a wise one.</p>
    <p>So take the first step to the best CV you can have. Contact me now.</p>
  </div>
  <div class="abs btn btn-white partner-btn">Contact <svg width="14" height="14" viewBox="0 0 16 16"><circle cx="8" cy="8" r="7" fill="#1b1b1b"/><path d="M6 4.5L9.5 8 6 11.5" stroke="#fff" stroke-width="2" fill="none"/></svg></div>
  <div class="abs partner-photo" role="img" aria-label="Photo of two professionals in conversation at a table in a high-rise office"></div>

  <!-- testimonials -->
  <h2 class="abs test-title serif">TESTIMONIALS</h2>
  <div class="abs rule" style="left:563px;top:3230px;width:74px"></div>

  <div class="abs tcard" style="left:111px">
    <div class="stars">★★★★★</div>
    <p>Lorem ipsum dolor sit amet, consectetur adipiscing elit, sed do eiusmod tempor incididunt ut labore et dolore magna aliqu ad minim veniam, quisea.</p>
    <hr>
    <div class="person"><div class="avatar" role="img" aria-label="Client portrait"></div><div><b>JOHN SMITH,</b><small>United States</small></div></div>
  </div>
  <div class="abs tcard" style="left:448px">
    <div class="stars">★★★★★</div>
    <p>Lorem ipsum dolor sit amet, consectetur adipiscing elit, sed do eiusmod tempor incididunt ut labore et dolore magna aliqu ad minim veniam, quisea.</p>
    <hr>
    <div class="person"><div class="avatar" role="img" aria-label="Client portrait"></div><div><b>LAURA,</b><small>United States</small></div></div>
  </div>
  <div class="abs tcard" style="left:784px">
    <div class="stars">★★★★★</div>
    <p>Lorem ipsum dolor sit amet, consectetur adipiscing elit, sed do eiusmod tempor incididunt ut labore et dolore magna aliqu ad minim veniam, quisea.</p>
    <hr>
    <div class="person"><div class="avatar" role="img" aria-label="Client portrait"></div><div><b>JOHN SMITH,</b><small>United States</small></div></div>
  </div>
  <div class="abs dots"><i></i><i class="on"></i><i></i><i></i></div>

  <!-- footer -->
  <svg class="abs" style="left:0;top:3605px" width="1200" height="477">
    <polygon points="0,150 960,10 962,40 0,185" fill="#eef0f6"/>
    <polygon points="0,10 330,100 0,140" fill="#0b65bf"/>
    <polygon points="0,178 1200,2 1200,477 0,477" fill="#1c1c1e"/>
  </svg>

  <div class="abs fcol" style="left:111px">
    <h4>Navigation</h4>
    <ul>
      <li><svg width="12" height="12" viewBox="0 0 16 16"><circle cx="8" cy="8" r="8" fill="#0b65bf"/><path d="M6.5 4.5L10 8l-3.5 3.5" stroke="#fff" stroke-width="2" fill="none"/></svg>Home</li>
      <li><svg width="12" height="12" viewBox="0 0 16 16"><circle cx="8" cy="8" r="8" fill="#0b65bf"/><path d="M6.5 4.5L10 8l-3.5 3.5" stroke="#fff" stroke-width="2" fill="none"/></svg>About Us</li>
      <li><svg width="12" height="12" viewBox="0 0 16 16"><circle cx="8" cy="8" r="8" fill="#0b65bf"/><path d="M6.5 4.5L10 8l-3.5 3.5" stroke="#fff" stroke-width="2" fill="none"/></svg>Services</li>
      <li><svg width="12" height="12" viewBox="0 0 16 16"><circle cx="8" cy="8" r="8" fill="#0b65bf"/><path d="M6.5 4.5L10 8l-3.5 3.5" stroke="#fff" stroke-width="2" fill="none"/></svg>Testimonials</li>
      <li><svg width="12" height="12" viewBox="0 0 16 16"><circle cx="8" cy="8" r="8" fill="#0b65bf"/><path d="M6.5 4.5L10 8l-3.5 3.5" stroke="#fff" stroke-width="2" fill="none"/></svg>Contact Us</li>
    </ul>
  </div>
  <div class="abs fcol" style="left:301px">
    <h4>Quick Links</h4>
    <ul>
      <li><svg width="12" height="12" viewBox="0 0 16 16"><circle cx="8" cy="8" r="8" fill="#0b65bf"/><path d="M6.5 4.5L10 8l-3.5 3.5" stroke="#fff" stroke-width="2" fill="none"/></svg>Site Map</li>
      <li><svg width="12" height="12" viewBox="0 0 16 16"><circle cx="8" cy="8" r="8" fill="#0b65bf"/><path d="M6.5 4.5L10 8l-3.5 3.5" stroke="#fff" stroke-width="2" fill="none"/></svg>Privacy Policy</li>
      <li><svg width="12" height="12" viewBox="0 0 16 16"><circle cx="8" cy="8" r="8" fill="#0b65bf"/><path d="M6.5 4.5L10 8l-3.5 3.5" stroke="#fff" stroke-width="2" fill="none"/></svg>Terms Of Use</li>
      <li><svg width="12" height="12" viewBox="0 0 16 16"><circle cx="8" cy="8" r="8" fill="#0b65bf"/><path d="M6.5 4.5L10 8l-3.5 3.5" stroke="#fff" stroke-width="2" fill="none"/></svg>Disclaimer</li>
    </ul>
  </div>
  <div class="abs fcol" style="left:491px;width:260px">
    <h4>Contact Info</h4>
    <div class="contact-item"><svg width="14" height="16" viewBox="0 0 24 30"><path fill="#0b65bf" d="M12 0a10 10 0 0110 10c0 8-10 20-10 20S2 18 2 10A10 10 0 0112 0zm0 6a4 4 0 100 8 4 4 0 000-8z"/></svg><div><b>LOCATION:</b>465, Lorem ipsum dolor sit amet,<br>United States</div></div>
    <div class="contact-item"><svg width="14" height="14" viewBox="0 0 24 24"><path fill="#0b65bf" d="M6.6 10.8a15 15 0 006.6 6.6l2.2-2.2c.3-.3.7-.4 1-.2 1.1.4 2.3.6 3.6.6.6 0 1 .4 1 1V20c0 .6-.4 1-1 1A17 17 0 013 4c0-.6.4-1 1-1h3.5c.6 0 1 .4 1 1 0 1.3.2 2.5.6 3.6.1.3 0 .7-.2 1z"/></svg><div><b>PHONE:</b>+1 (888) 888 8888</div></div>
    <div class="contact-item"><svg width="14" height="12" viewBox="0 0 24 18"><path fill="#0b65bf" d="M0 0h24v18H0zM2 2l10 7 10-7z"/></svg><div><b>EMAIL:</b>info@harbourlightcv.co.uk</div></div>
  </div>
  <div class="abs fcol" style="left:805px"><h4>Newsletter Signup</h4></div>
  <div class="abs news"><span>Email Address</span><b>SIGN UP</b></div>
  <div class="abs social footer-social" aria-label="Social links"><i class="on"></i><i></i><i></i></div>

  <div class="abs copyline"></div>
  <p class="abs copy">© 2024 <b>THE HARBOURLIGHT CV CONSULTANT</b> &nbsp;|&nbsp; All Rights Reserved</p>
</div>
</body>
</html>
```